Webdesign für Baustoffhandel
Zielgruppe
Baustoffhandel - stationär sowie online
Aufgabenstellung
moder, witzig, evtl. Comic charakter, logo ist ähnlich dem Tarnivel(Spiel) Männchen, farbig, Möglichkeit shop zu integrieren
siehe Logo bild

```html
<!DOCTYPE html>
<html lang="de">
<head>
<meta charset="utf-8">
<title>Der Baustoffgraf – Baustoffhandel</title>
<link href="https://fonts.googleapis.com/css2?family=Caveat+Brush&family=Roboto:wght@400;500;700&display=swap" rel="stylesheet">
<style>
:root{
  --blue:#0633a3;
  --orange:#f47b20;
  --teal:#0b3b55;
  --light:#f4f4f4;
  --text:#444;
  --white:#fff;
}
*{box-sizing:border-box;margin:0;padding:0}
html,body{width:1200px;height:3226px;overflow:hidden}
body{position:relative;background:var(--white);font-family:'Roboto',sans-serif;color:var(--text)}
.abs{position:absolute}
.hand{font-family:'Caveat Brush',cursive;color:var(--teal);font-weight:400}
.label{font-size:13px;color:var(--orange);text-transform:uppercase;font-weight:500}

.topbar{left:0;top:0;width:1200px;height:34px;background:var(--blue);color:#fff;font-size:10px;font-weight:500}
.topbar .item{position:absolute;top:11px;display:flex;align-items:center;gap:6px}
.navbar{left:0;top:34px;width:1200px;height:48px;background:var(--light)}
.navbar nav{position:absolute;right:194px;top:16px;display:flex;gap:30px;font-size:12px;font-weight:500;color:#222}
.navbar nav .active{color:var(--orange)}
.logo{left:194px;top:0;width:129px;height:82px;background:#fff;box-shadow:0 2px 6px rgba(0,0,0,.08);display:flex;align-items:flex-end;justify-content:center;padding-bottom:8px}
.logo span{font-family:'Roboto',sans-serif;font-weight:700;font-size:12px;color:#111}

.hero{left:0;top:82px;width:1200px;height:532px;background:var(--blue)}
.hero h1{position:absolute;left:194px;top:100px;font-family:'Caveat Brush',cursive;font-size:60px;line-height:66px;color:#fff;font-weight:400}
.hero p{position:absolute;left:194px;top:250px;width:420px;font-size:17px;line-height:29px;color:#fff}
.hero .character{position:absolute;left:714px;top:87px;width:457px;height:445px;border-radius:200px 200px 0 0;background:linear-gradient(180deg,#1a1a2e,#2b2b45 60%,#e0a050)}

.feature{top:545px;width:257px;height:172px;background:var(--light);box-shadow:0 6px 14px rgba(0,0,0,.08);padding:24px 33px}
.feature .icon{width:38px;height:38px;background:var(--orange);border-radius:2px;display:flex;align-items:center;justify-content:center}
.feature h3{font-family:'Caveat Brush',cursive;font-size:20px;color:var(--teal);font-weight:400;margin-top:12px}
.feature p{font-size:9.5px;line-height:15px;margin-top:6px}

.greypanel{left:0;top:656px;width:403px;height:534px;background:var(--light)}
.greyband{left:0;top:1190px;width:1200px;height:253px;background:var(--light)}
.worker{left:226px;top:777px;width:315px;height:430px;border-radius:160px;background:radial-gradient(circle at 50% 62%,#b7dbee 0 60%,transparent 61%),linear-gradient(180deg,transparent 0 10%,#e9b400 10% 90%,transparent 90%);}
.why{left:609px;top:812px;width:320px}
.why h2{font-size:32px;line-height:35px;margin-top:6px}
.why p{font-size:9.5px;line-height:15px;margin-top:12px}
.why ul{list-style:none;margin-top:12px}
.why li{display:flex;align-items:center;gap:14px;font-family:'Caveat Brush',cursive;font-size:19px;color:var(--teal);height:31px}

.brands h2{position:absolute;left:0;width:1200px;top:1238px;text-align:center;font-size:33px}
.brands p{position:absolute;left:440px;width:320px;top:1282px;text-align:center;font-size:9.5px;line-height:15px}
.brandrow{left:-20px;top:1334px;width:1240px;height:63px;display:flex;align-items:center;justify-content:space-around;font-family:'Roboto',sans-serif;font-weight:700;font-size:30px;color:#222}

.recs h2{position:absolute;left:0;width:1200px;top:1550px;text-align:center;font-size:33px;line-height:35px}
.recs p.sub{position:absolute;left:0;width:1200px;top:1637px;text-align:center;font-size:10px}
.rec{top:1707px;width:262px;height:168px;background:#fff;box-shadow:0 4px 14px rgba(0,0,0,.08);padding:22px 23px}
.rec h3{font-size:16px;font-weight:500;color:var(--teal);margin-top:8px}
.rec p{font-size:9.5px;line-height:15px;margin-top:10px}
.rec a{display:block;font-size:10px;color:var(--orange);margin-top:8px;text-decoration:none}
.btn{left:537px;top:1908px;width:125px;height:35px;background:var(--teal);color:#fff;font-size:11px;display:flex;align-items:center;justify-content:center;gap:6px}

.warehouse{left:0;top:2032px;width:570px;height:429px;background:linear-gradient(160deg,#8c8c88,#d9d4c8 55%,#efece6)}
.testi-head{left:606px;top:2033px;width:420px}
.testi-head h2{font-size:32px;line-height:36px;margin-top:6px}
.testi-head p{font-size:9.5px;line-height:15px;margin-top:14px}
.quote{top:2196px;height:224px;background:#f7f7f7;padding:32px 30px}
.quote .stars{color:#f7b21b;font-size:15px;letter-spacing:3px}
.quote q{display:block;font-style:italic;font-size:12px;line-height:19px;margin-top:12px;quotes:"„" "“"}
.quote hr{border:0;border-top:1px solid #ccc;margin:30px 0 22px}
.quote .name{font-size:14px;font-weight:500;color:var(--teal)}
.quote .role{font-size:9px;margin-top:2px}
.dots{left:836px;top:2441px;display:flex;gap:2px}
.dots span{width:5px;height:5px;background:#555}
.dots span:first-child{background:var(--orange)}

.prods{left:194px;top:2640px;width:420px}
.prods h2{font-size:33px;line-height:36px;margin-top:6px}
.prods p{font-size:9.5px;line-height:15px;margin-top:12px}
.arrows{left:954px;top:2724px;display:flex;gap:4px}
.arrows span{width:24px;height:24px;background:var(--orange);color:#fff;font-size:13px;display:flex;align-items:center;justify-content:center}
.prod{top:2810px;width:260px;height:312px;border:1px solid #ddd;background:#fff;padding:28px 18px}
.prod h3{font-family:'Caveat Brush',cursive;font-size:18px;line-height:20px;color:var(--teal);font-weight:400}
.prod .price{font-size:22px;font-weight:500;color:var(--orange);margin-top:6px}
.prod .img{position:absolute;left:50%;transform:translateX(-50%);bottom:22px;width:150px;height:150px}
</style>
</head>
<body>

<header>
  <div class="abs topbar">
    <div class="item" style="left:712px">
      <svg width="12" height="12" viewBox="0 0 24 24" fill="none" stroke="#fff" stroke-width="2"><path d="M22 16.9v3a2 2 0 0 1-2.2 2 19.8 19.8 0 0 1-8.6-3 19.5 19.5 0 0 1-6-6A19.8 19.8 0 0 1 2.1 4.2 2 2 0 0 1 4.1 2h3a2 2 0 0 1 2 1.7c.1 1 .4 1.9.7 2.8a2 2 0 0 1-.5 2.1L8 9.9a16 16 0 0 0 6 6l1.3-1.3a2 2 0 0 1 2.1-.4c.9.3 1.8.6 2.8.7a2 2 0 0 1 1.7 2z"/></svg>
      03581-40927</div>
    <div class="item" style="left:830px">
      <svg width="12" height="12" viewBox="0 0 24 24" fill="none" stroke="#fff" stroke-width="2"><path d="M12 22s7-6.3 7-12a7 7 0 0 0-14 0c0 5.7 7 12 7 12z"/><circle cx="12" cy="10" r="2.5"/></svg>
      Lindenstieg 14, 02999 Erlenau</div>
  </div>
  <div class="abs navbar">
    <nav><span class="active">Start</span><span>Sortiment</span><span>Services</span><span>Angebote</span><span>Über Uns</span><span>Kontakt</span></nav>
  </div>
  <div class="abs logo"><span>BAUSTOFFGRAF</span></div>
</header>

<section class="abs hero">
  <h1>Der Baustoffgraf –<br>Wo Qualität regiert.</h1>
  <p>Ihr Partner für Bauunternehmen, Handwerker und Heimwerker – zuverlässig, schnell, vor Ort.</p>
  <div class="character" role="img" aria-label="Comicfigur mit Zylinder und Schnurrbart, die einen Stapel Ziegel hält"></div>
</section>

<div class="abs greypanel"></div>
<div class="abs greyband"></div>

<div class="abs feature" style="left:194px">
  <div class="icon"><svg width="20" height="20" viewBox="0 0 24 24" fill="none" stroke="#fff" stroke-width="2"><circle cx="10" cy="10" r="6"/><path d="M15 15l6 6"/></svg></div>
  <h3>Jetzt Sortiment entdecken</h3>
  <p>Von Ziegel bis Dämmung – entdecken Sie unsere große Auswahl an hochwertigen Baustoffen für jedes Projekt.</p>
</div>
<div class="abs feature" style="left:471px">
  <div class="icon"><svg width="20" height="20" viewBox="0 0 24 24" fill="none" stroke="#fff" stroke-width="2"><path d="M22 16.9v3a2 2 0 0 1-2.2 2 19.8 19.8 0 0 1-8.6-3 19.5 19.5 0 0 1-6-6A19.8 19.8 0 0 1 2.1 4.2 2 2 0 0 1 4.1 2h3a2 2 0 0 1 2 1.7c.1 1 .4 1.9.7 2.8a2 2 0 0 1-.5 2.1L8 9.9a16 16 0 0 0 6 6l1.3-1.3a2 2 0 0 1 2.1-.4c.9.3 1.8.6 2.8.7a2 2 0 0 1 1.7 2z"/></svg></div>
  <h3>Kontakt aufnehmen</h3>
  <p>Sie haben Fragen oder brauchen Beratung? Unser Team steht Ihnen mit Fachwissen und Erfahrung zur Seite.</p>
</div>
<div class="abs feature" style="left:749px">
  <div class="icon"><svg width="20" height="20" viewBox="0 0 24 24" fill="none" stroke="#fff" stroke-width="2"><path d="M3 11l9-7 9 7v10H3z"/><path d="M9 21v-6h6v6"/></svg></div>
  <h3>Angebot anfordern</h3>
  <p>Unkompliziert anfragen. Persönlich beraten lassen.</p>
</div>

<div class="abs worker" role="img" aria-label="Comic-Handwerker in gelber Latzhose mit Werkzeugkasten und Schraubenschlüssel vor hellblauem Kreis"></div>

<section class="abs why">
  <div class="label">Warum der Graf?</div>
  <h2 class="hand">Darum bauen Profis<br>mit dem Grafen</h2>
  <p>Verlässlichkeit, Fachwissen und ein Sortiment, das keine Wünsche offenlässt – beim Baustoffgraf wissen Profis, was sie bekommen: Qualität, auf die man bauen kann.</p>
  <ul>
    <li><svg width="22" height="22" viewBox="0 0 24 24" fill="none" stroke="#f47b20" stroke-width="1.5"><rect x="3" y="5" width="18" height="15"/><path d="M8 12h8M8 16h8"/></svg>Große Lagerverfügbarkeit</li>
    <li><svg width="22" height="22" viewBox="0 0 24 24" fill="none" stroke="#f47b20" stroke-width="1.5"><path d="M2 12l5-4 5 3 5-3 5 4-7 5z"/></svg>Persönliche Fachberatung</li>
    <li><svg width="22" height="22" viewBox="0 0 24 24" fill="none" stroke="#f47b20" stroke-width="1.5"><rect x="2" y="7" width="12" height="9"/><path d="M14 10h4l3 3v3h-7"/><circle cx="6" cy="18" r="2"/><circle cx="17" cy="18" r="2"/></svg>Schnelle Lieferung</li>
    <li><svg width="22" height="22" viewBox="0 0 24 24" fill="none" stroke="#f47b20" stroke-width="1.5"><path d="M12 22s7-6.3 7-12a7 7 0 0 0-14 0c0 5.7 7 12 7 12z"/><circle cx="12" cy="10" r="2.5"/></svg>Regional &amp; nah</li>
  </ul>
</section>

<section class="brands">
  <h2 class="hand">Starke Marken für starke Projekte</h2>
  <p>Verlassen Sie sich auf bewährte Qualität – unsere Partner stehen für Innovation, Langlebigkeit und höchste Standards im Bauhandwerk.</p>
  <div class="abs brandrow">
    <span>RX</span><span>KARVO</span><span>TALWERK</span><span style="color:#666;font-weight:500">faserwolm</span><span>STIEGA</span><span>GRUNDEL</span><span>NORD</span>
  </div>
</section>

<section class="recs">
  <h2 class="hand">Grafs<br>Empfehlungen &amp; Aktionen</h2>
  <p class="sub">Entdecken Sie unsere aktuellen Highlights:</p>
  <div class="abs rec" style="left:194px">
    <svg width="38" height="38" viewBox="0 0 24 24" fill="none" stroke="#f47b20" stroke-width="1.2"><circle cx="15" cy="7" r="5"/><path d="M13 9l4-4M2 18l5-3h5l5 3-8 3z"/></svg>
    <h3>Sonderaktionen</h3>
    <p>Exklusive Rabatte und zeitlich begrenzte Angebote – nur für kurze Zeit!</p>
    <a>Read More &gt;</a>
  </div>
  <div class="abs rec" style="left:468px">
    <svg width="38" height="38" viewBox="0 0 24 24" fill="none" stroke="#f47b20" stroke-width="1.2"><rect x="3" y="8" width="18" height="13"/><path d="M3 12h18M3 16h18M9 8v13M15 8v13M7 3h8v5H7z"/></svg>
    <h3>Neue Produkte</h3>
    <p>Frisch eingetroffen: Entdecken Sie unsere neuesten Artikel und Innovationen.</p>
    <a>Read More &gt;</a>
  </div>
  <div class="abs rec" style="left:744px">
    <svg width="38" height="38" viewBox="0 0 24 24" fill="none" stroke="#f47b20" stroke-width="1.2"><rect x="2" y="9" width="13" height="10"/><path d="M5 13h7M5 16h5"/><circle cx="18" cy="7" r="3"/><path d="M18 1v2M23 7h-2M14 3l1 1"/></svg>
    <h3>Saisonale Tipps</h3>
    <p>Inspiration und Empfehlungen passend zur Jahreszeit – für ein stilvolles Zuhause.</p>
    <a>Read More &gt;</a>
  </div>
  <div class="abs btn">View All <svg width="10" height="10" viewBox="0 0 10 10" fill="none" stroke="#fff" stroke-width="1.2"><path d="M2 8l6-6M3 2h5v5"/></svg></div>
</section>

<div class="abs warehouse" role="img" aria-label="Foto einer Lagerhalle mit Regalen und Paletten voller Baustoffsäcke"></div>
<section class="abs testi-head">
  <div class="label">Kundenstimmen</div>
  <h2 class="hand">Vertrauen, das überzeugt –<br>von Profis und Heimwerkern</h2>
  <p>Unsere Kundschaft schätzt schnelle Abläufe und ehrliche Beratung. Lesen Sie hier, was andere über uns sagen.</p>
</section>
<div class="abs quote" style="left:436px;width:400px">
  <div class="stars">★★★★★</div>
  <q>Graf liefert immer erstklassige Materialien und fachkundige Beratung. Für meine Projekte kommt nichts anderes infrage.</q>
  <hr>
  <div class="name">Lena M.</div>
  <div class="role">Innenarchitektin</div>
</div>
<div class="abs quote" style="left:856px;width:400px;top:2193px">
  <div class="stars">★★★★★</div>
  <q>Große Auswahl, schnelle Lieferung und ein super Kundenservice. Mit Graf wird jedes Bauvorhaben einfacher.</q>
  <hr>
  <div class="name">Tom R.</div>
  <div class="role">Bauunternehmer</div>
</div>
<div class="abs dots"><span></span><span></span><span></span></div>

<section class="abs prods">
  <div class="label">Unsere Produktempfehlungen</div>
  <h2 class="hand">Entdecken Sie unsere<br>beliebtesten Baustoffe</h2>
  <p>Ob für Neubau, Renovierung oder kreative Projekte – hier finden Sie eine Auswahl an Produkten, die unsere Kund:innen besonders schätzen.</p>
</section>
<div class="abs arrows"><span>←</span><span>→</span></div>

<div class="abs prod" style="left:194px">
  <h3>Zementmörtel 30 kg – Mörtelix</h3>
  <div class="price">5,99 €</div>
  <div class="img" role="img" aria-label="Gelber Zementmörtel-Sack" style="background:linear-gradient(180deg,#f3e11a,#d9c400);width:105px;border-radius:8px"></div>
</div>
<div class="abs prod" style="left:471px">
  <h3>Steinhof Granitpflaster granit-grau 9 x 9 cm</h3>
  <div class="price">0,89 €</div>
  <div class="img" role="img" aria-label="Grauer Granitpflasterstein" style="background:radial-gradient(circle,#9a9a9a,#cfcfcf 70%,#fff 72%)"></div>
</div>
<div class="abs prod" style="left:748px">
  <h3>Isovant Hartschaumplatte XPS D N-III-L</h3>
  <div class="price">53,15 €</div>
  <div class="img" role="img" aria-label="Stapel hellgelber Dämmplatten mit Verpackung" style="background:linear-gradient(180deg,#f2ee3a 0 55%,#efe3bf 55%)"></div>
</div>
<div class="abs prod" style="left:1023px">
  <h3>Klebfix Montagekleber</h3>
  <div class="price">12,99 €</div>
  <div class="img" role="img" aria-label="Schwarze Kartusche Montagekleber" style="background:linear-gradient(90deg,#111,#333);width:45px;left:120px"></div>
</div>

</body>
</html>
```